New brand for digital company - your chance to get creative

We need to create a brand for our new business 'Lanternfish Digital'. Please read the brief below before progressing as we are looking for some quite specific outputs.

Background

We are positioning ourselves as ‘marketing technologists’ - we're helping businesses engage with their customers in the online space.

Our tactics include branding, marketing, online management, and social media, however we are differentiating ourselves by focusing on overall strategy, not just tactics. Our tagline is ‘Online made simple’.

We have stipulated some parameters for the brand but otherwise want designers to exercise their creativity.

Requirements
Must have
• We want to see an entire concept, not just a logo.

```html
<!DOCTYPE html>
<html lang="en">
<head>
<meta charset="utf-8">
<title>Lanternfish Digital – Brand Concept</title>
<link rel="stylesheet" href="https://fonts.googleapis.com/css2?family=Exo:wght@300;400;600;700&display=swap">
<style>
  :root {
    --sky: #6ec6f1;
    --sky-soft: #77caf4;
    --ink: #1a1a1a;
    --grey-text: #555;
    --paper: #ffffff;
    --backdrop: #e6e6e6;
    --photo-light: #d9d9d9;
    --photo-mid: #9a9a9a;
    --photo-dark: #3c3c3c;
  }
  * { margin: 0; padding: 0; box-sizing: border-box; }
  html, body { width: 1200px; height: 1000px; overflow: hidden; }
  body {
    position: relative;
    background: var(--backdrop);
    font-family: "Exo", sans-serif;
    color: var(--ink);
  }

  /* ---------- Poster ---------- */
  .poster {
    position: absolute; left: 50px; top: 42px; width: 687px; height: 918px;
    overflow: hidden; color: var(--paper);
  }
  .poster-photo {
    position: absolute; inset: 0;
    background:
      radial-gradient(ellipse at 75% 35%, rgba(255,255,255,0.55), transparent 55%),
      linear-gradient(180deg, var(--photo-light) 0%, var(--photo-mid) 55%, var(--photo-dark) 100%);
  }
  .poster-wordmark {
    position: absolute; left: 30px; top: 140px;
    font-size: 26px; font-weight: 600; color: var(--sky); letter-spacing: -0.2px;
  }
  .poster-headline { position: absolute; left: 30px; top: 242px; }
  .headline-bar {
    display: table; background: var(--sky); color: var(--paper);
    padding: 0 14px 0 2px; margin-bottom: 14px;
    font-size: 62px; line-height: 62px; letter-spacing: -0.5px;
  }
  .headline-bar.light { font-weight: 300; }
  .headline-bar.bold { font-weight: 600; }
  .poster-intro {
    position: absolute; left: 30px; top: 608px; width: 410px;
    font-size: 18px; font-weight: 300; line-height: 22px;
  }
  .poster-intro .accent { color: var(--sky); font-weight: 400; }
  .poster-tagline {
    position: absolute; left: 30px; top: 718px;
    font-size: 18px; font-weight: 300;
  }
  .poster-tagline .accent { color: var(--sky); font-weight: 600; }
  .poster-rule {
    position: absolute; left: 30px; top: 816px; width: 630px;
    border-top: 2px dotted rgba(255,255,255,0.8);
  }
  .poster-footer {
    position: absolute; left: 30px; top: 838px;
    display: flex; gap: 72px; font-size: 10px; line-height: 12px; font-weight: 300;
  }
  .poster-footer h4 { font-weight: 600; font-size: 10px; }
  .poster-footer-name {
    position: absolute; right: 28px; top: 852px;
    font-size: 12px; font-weight: 600;
  }

  /* ---------- Type specimen sheet ---------- */
  .type-sheet {
    position: absolute; left: 590px; top: 64px; width: 566px; height: 424px;
    background: var(--paper); padding: 0 23px;
  }
  .sheet-wordmark {
    position: absolute; left: 23px; top: 92px;
    font-size: 18px; font-weight: 600; color: var(--ink);
  }
  .sheet-rule {
    position: absolute; left: 23px; right: 23px; top: 131px;
    border-top: 1px dotted var(--sky);
  }
  .spec-label { font-size: 11px; color: var(--sky); }
  .spec-label span { color: var(--grey-text); }
  .headline-spec { position: absolute; left: 23px; top: 154px; }
  .headline-sample { margin-top: 6px; }
  .headline-sample div {
    display: table; background: var(--sky); color: var(--paper);
    font-size: 34px; font-weight: 400; line-height: 38px;
    padding: 0 6px 0 1px; margin-bottom: 5px; letter-spacing: 0.2px;
  }
  .spec-columns { position: absolute; left: 23px; top: 334px; width: 520px; }
  .spec-column { position: absolute; top: 0; }
  .spec-column.subheader { left: 0; }
  .spec-column.body-copy { left: 176px; }
  .spec-column.caption { left: 350px; }
  .spec-column .spec-sample { margin-top: 14px; }
  .subheader .spec-sample { font-size: 11px; line-height: 12px; }
  .subheader .spec-sample .lc { font-weight: 600; }
  .body-copy .spec-sample { font-size: 6px; line-height: 7px; margin-top: 10px; }
  .body-copy .spec-sample .lc { font-weight: 600; }
  .caption .spec-sample { font-size: 4px; line-height: 5px; margin-top: 6px; color: var(--grey-text); }

  /* ---------- Brand card ---------- */
  .brand-card {
    position: absolute; left: 765px; top: 506px; width: 392px; height: 452px;
    background: var(--sky-soft);
    display: flex; align-items: center; justify-content: center;
  }
  .card-wordmark {
    margin-top: 48px;
    font-size: 24px; font-weight: 600; color: var(--paper);
  }
</style>
</head>
<body>

  <section class="poster">
    <div class="poster-photo" role="img" aria-label="Black and white photo of an open-plan office with a blurred figure walking between desks and chairs"></div>

    <div class="poster-wordmark">Lanternfish Digital</div>

    <div class="poster-headline">
      <div class="headline-bar light">We Are</div>
      <div class="headline-bar bold">Lanternfish</div>
      <div class="headline-bar light">Digital</div>
    </div>

    <p class="poster-intro">
      We secialise in <span class="accent">branding, marketing, online management</span>, and <span class="accent">social media,</span> however we differenciate ourselves by focusing on overall strategy, not just tactics.
    </p>
    <p class="poster-tagline">We are...<span class="accent">online made simple</span></p>

    <div class="poster-rule"></div>
    <div class="poster-footer">
      <div>
        <h4>Address</h4>
        1 Street Name<br>Town, City<br>Zip Code, Country
      </div>
      <div>
        <h4>Contact</h4>
        +61 (02) 7010 4827<br>www.lanternfishdigital.com<br>info@lanternfishdigital.com
      </div>
    </div>
    <div class="poster-footer-name">Lanternfish Digital</div>
  </section>

  <section class="type-sheet">
    <div class="sheet-wordmark">Lanternfish Digital</div>
    <div class="sheet-rule"></div>

    <div class="headline-spec">
      <div class="spec-label">Headline <span>(72 /84.4px)</span></div>
      <div class="headline-sample">
        <div>abcdefghijklmnopqrstuvwxy</div>
        <div>ABCDEFGDEFGHIJKLIMN</div>
        <div>0123456789!@£$</div>
      </div>
    </div>

    <div class="spec-columns">
      <div class="spec-column subheader">
        <div class="spec-label">Subheader <span>(21 /24px)</span></div>
        <div class="spec-sample"><span class="lc">abcdefghijklmnopqrstuvwxyz</span><br>ABCDEFGHIJKVWXYZ<br>0123456789!@£$</div>
      </div>
      <div class="spec-column body-copy">
        <div class="spec-label">BodyCopy <span>(12 /15px)</span></div>
        <div class="spec-sample"><span class="lc">abcdefghijklmnopqrstuvwxyz</span><br>ABCDEFGHIJKLMNOPQRSTUVWXYZ<br>0123456789!@£$</div>
      </div>
      <div class="spec-column caption">
        <div class="spec-label">Caption <span>(8/9px)</span></div>
        <div class="spec-sample">abcdefghijklmnopqrstuvwxyz<br>ABCDEFGHIJKLMNOPQRSTUVWXYZ<br>0123456789!@£$</div>
      </div>
    </div>
  </section>

  <section class="brand-card">
    <div class="card-wordmark">Lanternfish Digital</div>
  </section>

</body>
</html>
```